Promotional Flyer/Email Design - Cabling services for Broadcast and Audio Visual

We need a promotional flyer/email design to help launch our company, Velto Wire. We provide cabling services for Broadcast Television and Audio Visual systems. Recent projects include major television events such as the Harrowfield Racquet Open and Audio Visual/Entertainment systems for wealthy clients in their homes and on-board super yachts.

The flyer will be printed as single sided A5 and also be sent out in the body of a promotional email. It should feature the company logo along with a complementary colour scheme. It should have a clean finish with images that show the type of work we do (cabling and equipment installation) or the setting for these systems (tv studio, super yacht, cinema room, meeting room with projector etc.)

Services we offer are:

Broadcast/AV system design
On-site installation
Rack building
Pre-fabricated cable looms
Fibre optic installation

About the company:

Velto Wire provide cabling services for Broadcast Television and Audio Visual systems. With over 15 years experience working in these industries we can help with every aspect of design, project managment, installation and maintenance. Our projects range from fibre optic cabling at major sports events to installing and commisioning bespoke control systems on some of the worlds largest super yachts.

Contact details:

To get a quote or discuss your project contact us now
Telephone: TBC
Email: info@velto-wire.example
Website: www.velto-wire.example
Address: TBC

Other information:

The company is based in London, UK. Our projects often take place in other countries with work taking place accross Europe and beyond.

We have a London based workshop for rack building and cable pre-fabrication.

Our website is www.velto-wire.example

Images:

Images attached can be editted for use on the flyer or have ideas taken from them. Only the company logo is required to feature on the final design.

Target Market(s)

Business to business

Industry/Entity Type

It Company

Font styles to use
Sans Serif

Requirements
Must have
• Company logo
• List of services
• Contact details
Nice to have
• Image of cabling, home cinema room, super yacht, luxury home, outside broadcast truck, fibre optic equipment or cabling.

```html
<!DOCTYPE html>
<html lang="en">
<head>
<meta charset="utf-8">
<title>Velto Wire – Broadcast &amp; AV System Installation</title>
<link href="https://fonts.googleapis.com/css2?family=Anton&family=Open+Sans:wght@400;600&display=swap" rel="stylesheet">
<style>
  :root{
    --blue:#4d86e6;
    --blue-soft:#8fb3f2;
    --red:#cf1545;
    --ink:#1f1f24;
    --paper:#ffffff;
    --stage:#d9dadd;
    --photo-light:#c9c7c2;
    --photo-dark:#55524f;
  }
  *{box-sizing:border-box;margin:0;padding:0}
  html,body{width:1200px;height:984px;overflow:hidden;background:var(--stage)}
  body{font-family:"Open Sans",sans-serif;color:var(--ink)}
  .flyer{position:absolute;left:220px;top:22px;width:760px;height:940px;background:var(--paper);overflow:hidden;box-shadow:0 6px 24px rgba(0,0,0,.25)}
  .flyer-frame{position:absolute;inset:0}
  .logo-box{position:absolute;left:520px;top:300px;width:210px;height:76px;background:var(--paper);border:3px solid var(--ink);border-radius:12px;display:flex;align-items:center;justify-content:center;gap:10px}
  .logo-mark{width:16px;height:16px;background:var(--red)}
  .logo-name{font-family:"Open Sans",sans-serif;font-weight:600;font-size:26px;color:var(--ink)}
  .headline{position:absolute;left:120px;top:418px;font-family:"Anton",sans-serif;line-height:1}
  .headline-sub{display:block;color:var(--blue-soft);font-size:34px;letter-spacing:.5px}
  .headline-main{display:block;color:var(--red);font-size:74px;letter-spacing:1px;margin-top:-2px}
  .heading{font-family:"Anton",sans-serif;font-size:21px;letter-spacing:.5px;line-height:1.1}
  .heading.red{color:var(--red)}
  .heading.blue{color:var(--blue)}
  .heading.white{color:var(--paper)}
  .service-list{list-style:none;font-size:15px;line-height:1.7}
  .service-list li{display:flex;align-items:center;gap:8px;white-space:nowrap}
  .service-list li::before{content:"";width:11px;height:11px;border-radius:50%;background:var(--ink);flex:none}
  .services{position:absolute;left:40px;top:560px}
  .services-mid{position:absolute;left:285px;top:530px}
  .services-top{position:absolute;left:560px;top:470px}
  .services-top li{align-items:flex-start;line-height:1.25}
  .services-top li::before{margin-top:4px}
  .about{position:absolute;left:40px;top:640px;width:375px}
  .about p{font-size:15.5px;line-height:1.4;text-align:justify;margin-top:4px}
  .contact{position:absolute;left:40px;top:790px;width:400px}
  .contact p{font-size:15.5px;line-height:1.3;margin-top:4px}
  .contact-email{position:absolute;left:190px;top:66px;display:flex;align-items:center;gap:6px;font-size:14px;white-space:nowrap}
  .contact-line{display:flex;align-items:center;gap:8px;font-size:20px;line-height:1.15}
  .contact-lines{margin-top:10px}
  .info-panel{position:absolute;left:450px;top:588px;width:310px;height:352px;background:var(--blue);border-top-left-radius:34px;color:var(--paper);padding:22px 24px 0 26px}
  .info-panel p{font-size:14px;line-height:1.4;text-align:justify}
  .info-panel .heading{margin-top:12px;margin-bottom:4px}
  .web{display:flex;align-items:center;gap:8px;font-weight:600;font-size:16px;margin-top:10px;white-space:nowrap}
  svg.icon{flex:none}
</style>
</head>
<body>
<main class="flyer">
  <svg class="flyer-frame" width="760" height="940" viewBox="0 0 760 940">
    <defs>
      <linearGradient id="roomTones" x1="0" y1="0" x2="1" y2="1">
        <stop offset="0" stop-color="#c9c7c2"/>
        <stop offset=".55" stop-color="#9c9995"/>
        <stop offset="1" stop-color="#55524f"/>
      </linearGradient>
    </defs>
    <path d="M0 400 C160 390 260 360 400 370 C560 380 660 350 760 330 L760 940 L0 940 Z" fill="#4d86e6"/>
    <path d="M20 412 C170 400 270 372 410 382 C560 392 660 362 760 346 L760 940 L110 940 C60 940 20 905 20 860 Z" fill="#ffffff"/>
    <path d="M0 0 H760 V330 C660 350 560 372 400 362 C260 352 160 382 0 392 Z" fill="url(#roomTones)" role="img" aria-label="Photo of a modern living room with an equipment rack, wall-mounted TV and floor-standing speakers"/>
  </svg>

  <div class="logo-box">
    <span class="logo-mark"></span>
    <span class="logo-name">Velto Wire</span>
  </div>

  <h1 class="headline">
    <span class="headline-sub">BROADCAST &amp; AV SYSTEM</span>
    <span class="headline-main">INSTALLATION</span>
  </h1>

  <ul class="service-list services-top">
    <li>Broadcast/<br>AV system design</li>
  </ul>

  <ul class="service-list services-mid">
    <li>Fibre optic installation</li>
    <li>Pre-fabricated cable looms</li>
  </ul>

  <section class="services">
    <h2 class="heading red">SERVICES:</h2>
    <ul class="service-list">
      <li>Rack building</li>
      <li>On-site installation</li>
    </ul>
  </section>

  <section class="about">
    <h2 class="heading blue">ABOUT THE COMPANY:</h2>
    <p>Velto Wire provide cabling services for Broadcast Television and Audio Visual systems. With over 15 years experience working in these industries we can help with every aspect of design, project managment, installation &amp; maintenance.</p>
  </section>

  <section class="contact">
    <h2 class="heading red">CONTACT DETAILS:</h2>
    <p>To get a quote or discuss your project<br>contact us now</p>
    <div class="contact-email">
      <svg class="icon" width="18" height="14" viewBox="0 0 18 14"><rect x="1" y="1" width="16" height="12" rx="1" fill="#4d86e6"/><path d="M1 2 L9 8 L17 2" stroke="#fff" stroke-width="1.5" fill="none"/></svg>
      info@velto-wire.example
    </div>
    <div class="contact-lines">
      <div class="contact-line">
        <svg class="icon" width="20" height="18" viewBox="0 0 20 18"><path d="M2 6 C2 2 18 2 18 6 L15 8 L13 5 H7 L5 8 Z" fill="#4d86e6"/><rect x="4" y="9" width="12" height="8" rx="2" fill="#4d86e6"/></svg>
        TBC
      </div>
      <div class="contact-line">
        <svg class="icon" width="20" height="22" viewBox="0 0 20 22"><path d="M10 1 C5 1 2 4.5 2 8.5 C2 14 10 21 10 21 C10 21 18 14 18 8.5 C18 4.5 15 1 10 1 Z" fill="#4d86e6"/><circle cx="10" cy="8.5" r="3" fill="#fff"/></svg>
        TBC
      </div>
    </div>
  </section>

  <section class="info-panel">
    <p>Our projects range from fibre optic cabling at major sports events to installing and commisioning bespoke control systems on some of the worlds largest super yachts.</p>
    <h2 class="heading white">OTHER INFORMATION:</h2>
    <p>The company is based in London, UK. Our projects often take place in other countries with work taking place accross Europe and beyond.</p>
    <p>We have a London based workshop for rack building and cable pre-fabrication.</p>
    <div class="web">
      <svg class="icon" width="20" height="20" viewBox="0 0 20 20" fill="none" stroke="#fff" stroke-width="1.6"><circle cx="10" cy="10" r="8.5"/><ellipse cx="10" cy="10" rx="3.8" ry="8.5"/><path d="M1.5 10 H18.5 M3 5.5 H17 M3 14.5 H17"/></svg>
      www.velto-wire.example
    </div>
  </section>
</main>
</body>
</html>
```